Trade Show Booth Sign Design for Retracting Banner

I need a trade show booth sign designed. It will be for a retractable banner that is double sided with 34 by 81 inch.

I want to incorporate my logo (see attached, have it in other file formats as well) and graphics from my website (https://www.dolbrookteachingadvisory.com/) with parts or all of the following text.

· Educational Content Creation
o Supplemental Textbook Content Development
o E-learning Content Development
· Curriculum Development
o KVTR/Bright Ladder
o Three Dimensional Learning
· Assessment
o Formative Assessments
o Elementary School, Middle School, High School, College, and Business
· Professional Development
o Training
o Facilitation

Target Market(s)

Education

Industry/Entity Type

Education

Font styles to use
Sans Serif

Colors

Designer to choose colors to be used in the design.

Requirements
Must have
• Eye catching and easy to read design
Nice to have
• Would like to see incorporation of my logo and some of the elements of my website images
Should not have
• N/A

```html
<!DOCTYPE html>
<html lang="en">
<head>
<meta charset="utf-8">
<title>Dolbrook Teaching Advisory – Retractable Banner</title>
<link href="https://fonts.googleapis.com/css2?family=Montserrat:wght@400;500;800&display=swap" rel="stylesheet">
<style>
  :root {
    --sky-top: #1a7fc6;
    --sky-mid: #33c3c6;
    --sky-low: #2a9fd0;
    --sky-bottom: #5b8fd6;
    --navy: #0c2a5e;
    --navy-soft: #1f3f78;
    --orange: #f4592d;
    --white: #ffffff;
    --ring: #c9d1d8;
    --bulb-red: #e8413a;
    --bulb-blue: #3a63d8;
    --bulb-yellow: #f6c915;
    --bulb-orange: #f6861f;
    --bulb-sky: #8cc8ec;
  }
  * { margin: 0; padding: 0; box-sizing: border-box; }
  html, body { width: 1200px; height: 2857px; overflow: hidden; }
  body {
    position: relative;
    font-family: "Montserrat", sans-serif;
    color: var(--white);
    background: linear-gradient(180deg, var(--sky-top) 0%, var(--sky-mid) 30%, var(--sky-low) 55%, var(--sky-bottom) 100%);
  }
  .art { position: absolute; }
  .art--bulbs {
    left: 40px; top: 0; width: 1120px; height: 300px;
    background:
      radial-gradient(circle at 6% 35%, rgba(232,65,58,0.85) 0 60px, transparent 95px),
      radial-gradient(circle at 27% 60%, rgba(58,99,216,0.85) 0 62px, transparent 97px),
      radial-gradient(circle at 50% 78%, rgba(246,201,21,0.9) 0 66px, transparent 105px),
      radial-gradient(circle at 72% 30%, rgba(246,134,31,0.85) 0 62px, transparent 97px),
      radial-gradient(circle at 93% 60%, rgba(140,200,236,0.9) 0 62px, transparent 97px);
  }
  .art--supplies {
    left: 905px; top: 648px; width: 295px; height: 800px;
    background:
      radial-gradient(circle at 40% 14%, rgba(40,60,80,0.55) 0 70px, transparent 110px),
      radial-gradient(circle at 75% 40%, rgba(246,170,40,0.75) 0 90px, transparent 140px),
      radial-gradient(circle at 35% 72%, rgba(40,60,80,0.5) 0 70px, transparent 110px),
      radial-gradient(circle at 85% 78%, rgba(232,80,50,0.7) 0 60px, transparent 100px),
      radial-gradient(circle at 80% 20%, rgba(160,230,170,0.55) 0 50px, transparent 85px);
  }
  .art--maths {
    left: 0; top: 2314px; width: 381px; height: 543px;
    background:
      radial-gradient(circle at 12% 12%, rgba(232,65,58,0.8) 0 50px, transparent 85px),
      radial-gradient(circle at 48% 16%, rgba(246,170,40,0.8) 0 70px, transparent 110px),
      radial-gradient(circle at 55% 48%, rgba(255,255,255,0.75) 0 60px, transparent 100px),
      radial-gradient(circle at 18% 82%, rgba(232,80,90,0.7) 0 60px, transparent 100px),
      radial-gradient(circle at 60% 85%, rgba(140,200,236,0.7) 0 45px, transparent 80px);
  }
  .cloud-band {
    position: absolute; left: 0; top: 2200px; width: 1200px; height: 657px;
    background: linear-gradient(180deg, rgba(255,255,255,0) 0%, rgba(255,255,255,0.14) 12%, rgba(255,255,255,0.08) 100%);
  }
  .badge { position: absolute; border-radius: 50%; border: 12px solid var(--ring); }
  .badge--presentation {
    left: 34px; top: 1476px; width: 376px; height: 372px;
    background:
      radial-gradient(ellipse 48% 32% at 42% 36%, rgba(255,255,255,0.85) 0 98%, transparent 100%),
      radial-gradient(ellipse 40% 16% at 45% 86%, rgba(20,30,50,0.7) 0 98%, transparent 100%),
      var(--navy);
  }
  .badge--science {
    left: 785px; top: 1924px; width: 377px; height: 371px;
    background:
      radial-gradient(circle at 50% 52%, rgba(255,255,255,0.9) 0 48px, transparent 52px),
      radial-gradient(circle at 50% 50%, rgba(120,200,210,0.35) 0 140px, transparent 150px),
      var(--navy);
  }
  .badge--ideas {
    left: 810px; top: 2486px; width: 327px; height: 324px;
    border-color: #d6dde3;
    background:
      radial-gradient(circle at 55% 50%, rgba(246,201,21,0.85) 0 40px, transparent 60px),
      #ffffff;
  }

  .brand {
    position: absolute; left: 0; top: 318px; width: 1200px;
    text-align: center; color: var(--navy);
    font-weight: 800; text-transform: uppercase;
  }
  .brand__name { display: block; font-size: 158px; line-height: 200px; letter-spacing: 2px; }
  .brand__tagline { display: block; font-size: 62px; line-height: 86px; letter-spacing: 1px; }

  .intro {
    position: absolute; left: 97px; top: 657px; width: 760px;
    font-size: 34px; line-height: 44px; letter-spacing: 1.2px;
    text-align: justify; font-weight: 400;
  }
  .service-title {
    position: absolute; background: var(--orange);
    font-weight: 500; font-size: 50px; letter-spacing: 1px;
    display: flex; align-items: center;
  }
  .service-title--content { left: 0; top: 1072px; width: 891px; height: 118px; padding-left: 42px; }
  .service-title--curriculum { left: 419px; top: 1511px; width: 781px; height: 118px; padding-left: 48px; }
  .service-title--assessment { left: 0; top: 1901px; width: 709px; height: 115px; justify-content: center; }
  .service-title--pd { left: 389px; top: 2343px; width: 811px; height: 114px; padding-left: 32px; }

  .service-list { position: absolute; list-style: none; font-size: 40px; line-height: 50px; letter-spacing: 1px; }
  .service-list li { position: relative; margin-bottom: 24px; }
  .service-list li::before {
    content: ""; position: absolute; left: -40px; top: 17px;
    width: 18px; height: 18px; border-radius: 50%; background: var(--orange);
  }
  .service-list--content { left: 120px; top: 1236px; width: 720px; }
  .service-list--curriculum { left: 495px; top: 1684px; width: 680px; }
  .service-list--assessment { left: 131px; top: 2061px; width: 640px; }
  .service-list--assessment li { margin-bottom: 22px; }
  .service-list--pd { left: 495px; top: 2505px; width: 300px; }
</style>
</head>
<body>
  <div class="art art--bulbs" role="img" aria-label="Illustration of crumpled paper light bulbs in red, blue, yellow, orange and light blue hanging from cords"></div>
  <div class="art art--supplies" role="img" aria-label="Illustration of school supplies: graduation cap, crayons, beaker, set square, magnifying glass and book"></div>
  <div class="cloud-band"></div>
  <div class="art art--maths" role="img" aria-label="Illustration of maths and science items: clock, protractor, paper plane, flasks and formulas"></div>

  <div class="badge badge--presentation" role="img" aria-label="Illustration of a presenter showing research charts to an audience"></div>
  <div class="badge badge--science" role="img" aria-label="Illustration of science and learning icons around a flask"></div>
  <div class="badge badge--ideas" role="img" aria-label="Illustration of a head outline with a light bulb and idea symbols"></div>

  <h1 class="brand"><span class="brand__name">Dolbrook</span><span class="brand__tagline">Teaching Advisory</span></h1>

  <p class="intro">Dolbrook Teaching Advisory delivers research-based educational products for both the K-16 and corporate settings. Dolbrook Teaching Advisory utilizes learning theory and content expertise to develop content that will stick with people (students or employees) and/or truly assess what they understand.</p>

  <h2 class="service-title service-title--content">Educational Content Creation</h2>
  <ul class="service-list service-list--content">
    <li>Supplemental Textbook<br>Content Development</li>
    <li>E-learning Content Development</li>
  </ul>

  <h2 class="service-title service-title--curriculum">Curriculum Development</h2>
  <ul class="service-list service-list--curriculum">
    <li>KVTR/Bright Ladder</li>
    <li>Three Dimensional Learning</li>
  </ul>

  <h2 class="service-title service-title--assessment">Assessment</h2>
  <ul class="service-list service-list--assessment">
    <li>Formative Assessments</li>
    <li>Elementary School, Middle School, High School, College, and Business</li>
  </ul>

  <h2 class="service-title service-title--pd">Professional Development</h2>
  <ul class="service-list service-list--pd">
    <li>Training</li>
    <li>Facilitation</li>
  </ul>
</body>
</html>
```